Relaunch / Responsives, modernes Webdesign für ein Campingportal
Zielgruppe
Die zeltwiese GmbH betreibt mit der Plattform www.zeltwiese-online.de eines der führenden Campingportale in Deutschland.
Im Zuge des Relaunches soll ein frisches, neues und modernes Design der Webseite erfolgen und auch die mobile Nutzbarkeit durch ein responsives Design verbessert werden.
Zielgruppe sind Camperinnen und Camper bzw. solche, die es vielleicht einmal werden wollen. Ebenso natürlich auch die Betreiber der Campingplätze, die Mitglied bei zeltwiese sein können und damit bei der Suche, auf der Karte und in den Regionen gefunden werden. Sie sind dann mit einer eigenen Campingplatzseite vertreten, auf der neben allen wichtigen Informationen auch Bilder und Videos vom Platz zu sehen sind.
Aktuell ist im Fokus ein Campingführer (Campingplatzsuche), der wie beschrieben auch per Karte erfolgt und mit Filtern eingeschränkt werden kann. Auch ein Blog ist vorhanden, es wird noch ein Forum geben usw.
Später wird auch noch ein Shop, etc. hinzukommen...
Aufgabenstellung
Das Design soll frisch, modern und natürlich responsiv sein. Das Logo ist dabei weiterhin gesetzt. Daran können Sie also z.B. die Farbgebung übernehmen (v.a. das Grün).
Das Design soll sich nicht mehr rein vertikal ausrichten (wie bisher) sondern horizontal über den gesamten Bildschirm.
Dabei muss z.B. auf der Startseite u.a. auch ein Feld vorhanden sein, in dem man Länder, Regionen oder direkt Campingplätze suchen kann uns sich ein Auswahlfeld mit den vorgeschlagenen Ergebnissen öffnet. So wie bei Hotelportalen zumeist auch.
Es gibt aktuell nachfolgende Seitentypen:
1. Startseite (bisher http://www.zeltwiese-online.de/)
Hier soll u.a. auch ein Feld zur Eingabe eines Landes, einer Region oder eines Platzes existieren, bei dem bei Eingabe Auswahlmöglichkeiten sichtbar werden (wie bei Reiseportalen).
So z.B. bei:
Urlaubsquartiere[Punkt]de
Logis Sofort
Reisepruefer
Auch eine Karte von Europa wäre hier ggf. interessant, die man dann beim Anklicken auf Deutschland fokussiert, danach dann weiter auf die Nordsee usw.
Zudem Flächen wo man besondere Themen oder Regionen noch einmal extra anführt "Campingplätze am Meer", "Campingplätze in den Bergen", "Campingplätze Stadtnah, usw.
Hier zum Beispiel dann auch später eine Grafik zum Shop usw.
Auch kann es einige Flächen geben, die man an Campingplätze vermieten kann, um auf der Startseite präsent zu sein. Also quasi einige exklusive Campingplätze.
Zudem sollte man einen Block haben, wo man besonders nachgefragte Regionenlinks vorstellen kann (Beliebte Reiseziele, Nordseeküste, Alpen, etc.).
Dies müssen aber keine Bilder sein, sondern können auch nur Links sein als Gruppe in einem Block.
Zudem muss es unten ein Textfeld geben, da es sonst schwer wird mit der Regionenseite bei Suchlux weiterhin gut zu ranken.
Selbstverständlich müssen auch Werbeflächen eingeplant sein für Suchlux adse..

```html
<!DOCTYPE html>
<html lang="de">
<head>
<meta charset="utf-8">
<title>zeltwiese – Campingplatzsuche</title>
<link href="https://fonts.googleapis.com/css2?family=Roboto:wght@400;500;700&display=swap" rel="stylesheet">
<style>
:root{
  --navy:#0b2460;
  --green:#7ab51d;
  --green-dark:#3f9100;
  --link:#0b2460;
  --text:#1d1d1d;
  --line:#e4e4e4;
  --panel:#f2f2f2;
  --ad-blue:#0a6fc9;
  --white:#fff;
}
*{box-sizing:border-box;margin:0;padding:0}
html,body{width:1200px;height:2261px;overflow:hidden;background:var(--white);font-family:'Roboto',sans-serif;color:var(--text)}
.page{position:relative;width:1200px;height:2261px}

.site-header{position:absolute;left:0;top:0;width:1200px;height:78px;background:var(--white)}
.brand{position:absolute;display:flex;align-items:center;gap:8px;font-weight:700;font-size:26px;color:var(--navy)}
.brand-dot{width:16px;height:16px;border-radius:50%;background:var(--green)}
.main-nav{position:absolute;top:14px;left:0;width:1200px;height:60px}
.nav-item{position:absolute;display:flex;flex-direction:column;align-items:center;font-size:14.5px;color:#222;gap:6px;transform:translateX(-50%);white-space:nowrap}
.nav-item svg{height:30px}
.nav-item.active{color:var(--green);font-weight:500}

.search-band{position:absolute;left:0;top:78px;width:1200px;height:99px;background:var(--navy)}
.search-field{position:absolute;left:272px;top:40px;width:559px;height:33px;background:var(--white);border:2px solid var(--green);display:flex;align-items:center;padding-left:37px;font-size:15px}
.search-field svg{position:absolute;left:8px;top:-12px}
.search-btn{position:absolute;left:839px;top:40px;width:90px;height:33px;background:var(--green);color:var(--white);font-size:15px;display:flex;align-items:center;justify-content:center}

.page-title{position:absolute;left:46px;top:208px;font-size:27px;font-weight:400}
.map-teaser{position:absolute;left:32px;top:264px;width:299px;height:179px;background:var(--panel);padding:12px 13px}
.map-art{position:relative;width:100%;height:100%;background:linear-gradient(135deg,#d9d6d3,#ece7e4 55%,#cfd0cf);overflow:hidden}
.map-label{position:absolute;left:70px;top:5px;width:140px;height:140px;border-radius:50%;background:rgba(255,255,255,.55);display:flex;align-items:flex-end;justify-content:center;padding-bottom:30px;font-size:24px;font-weight:500;color:var(--navy)}
.filter-box{position:absolute;left:32px;top:453px;width:299px;height:426px;border:1px solid var(--line)}
.filter-box h3{position:absolute;left:16px;top:18px;font-size:18.5px;font-weight:400}
.filter-list{position:absolute;left:17px;top:51px;list-style:none}
.filter-list li{display:flex;align-items:center;height:38px;margin-bottom:12px;font-size:15px}
.filter-icon{width:38px;height:38px;background:#e9e9e9;display:flex;align-items:center;justify-content:center;margin-right:16px}
.more-filters{position:absolute;left:21px;top:373px;font-size:18.5px;display:flex;align-items:center;gap:18px}
.ad-note{position:absolute;font-size:9px;color:#888}
.rect-ad{position:absolute;left:31px;top:914px;width:300px;height:250px;background:var(--green-dark);color:var(--white);display:flex;flex-direction:column;align-items:center;justify-content:center;text-align:center}
.rect-ad strong{font-size:29px;line-height:1.35;font-weight:700}
.rect-ad span{font-size:12px;margin-top:18px}

.camp-card{position:absolute;left:358px;width:812px;height:231px;border:1px solid var(--line);background:var(--white)}
.camp-photo{position:absolute;left:0;top:0;width:270px;height:229px}
.camp-body{position:absolute;left:289px;top:0;right:20px;height:100%}
.camp-body h2{position:absolute;top:10px;font-size:21.5px;font-weight:400;white-space:nowrap}
.camp-desc{position:absolute;top:45px;left:2px;font-size:14.6px;line-height:22px;color:#222}
.camp-meta{position:absolute;top:133px;left:2px;width:100%;font-size:14.6px;line-height:22px;display:grid;grid-template-columns:225px 1fr}
.camp-link{position:absolute;right:3px;bottom:10px;font-size:15px;font-weight:700;color:var(--link);text-decoration:underline}

.banner-ad{position:absolute;left:358px;width:813px;height:100px;background:var(--ad-blue);color:var(--white)}
.banner-art{position:absolute;top:18px;height:82px}
.banner-text{position:absolute;left:141px;top:16px}
.banner-text strong{display:block;font-size:22px;font-weight:700}
.banner-text span{display:block;font-size:17.5px;line-height:21px;margin-top:4px;color:#e6f0fb}
.banner-brand{position:absolute;left:662px;top:20px;font-size:16px;font-weight:500}
.banner-btn{position:absolute;left:651px;top:52px;width:131px;height:31px;border-radius:16px;background:var(--white);color:var(--ad-blue);font-size:15px;display:flex;align-items:center;justify-content:center}
.ad-label{position:absolute;left:359px;font-size:13px;font-style:italic;color:#666}

.site-footer{position:absolute;left:0;top:1609px;width:1200px;height:652px;background:var(--panel)}
.footer-col h2{position:absolute;top:24px;font-size:27px;font-weight:500}
.footer-text{position:absolute;left:35px;top:92px;width:370px;font-size:18.3px;line-height:22.5px}
.link-col{position:absolute;top:90px;list-style:none;font-size:18.3px}
.link-col li{height:37px}
.footer-rule{position:absolute;left:37px;top:463px;width:1120px;height:2px;background:#cfcfcf}
.footer-social{position:absolute;top:510px;left:360px;display:flex;align-items:center;gap:22px}
.social{display:flex;align-items:center;gap:6px;font-size:14px;color:var(--navy);font-weight:500}
.social-dot{width:14px;height:14px;border-radius:50%;border:2px solid var(--navy)}
.mail-btn{width:50px;height:50px;border-radius:50%;display:flex;align-items:center;justify-content:center;background:var(--navy)}
.footer-links{position:absolute;left:0;top:580px;width:1200px;text-align:center;font-size:18.3px;color:var(--navy)}
</style>
</head>
<body>
<div class="page">

<header class="site-header">
  <div class="brand" style="left:84px;top:23px"><span class="brand-dot"></span>zeltwiese</div>
  <nav class="main-nav">
    <div class="nav-item active" style="left:369px">
      <svg viewBox="0 0 34 30" width="34"><path d="M17 2 2 15h4v13h8v-8h6v8h8V15h4z" fill="var(--green)"/></svg>Home</div>
    <div class="nav-item" style="left:536px">
      <svg viewBox="0 0 30 30" width="30"><path d="M15 6 4 28h9l2-6 2 6h9z M10 2l5 7 5-7" fill="#111" stroke="#111" stroke-width="2"/></svg>Campingplätze</div>
    <div class="nav-item" style="left:732px">
      <svg viewBox="0 0 34 30" width="34"><ellipse cx="16" cy="15" rx="14" ry="11" fill="#111"/><path d="M6 23 3 29l9-4z" fill="#111"/><circle cx="10" cy="15" r="2" fill="#fff"/><circle cx="16" cy="15" r="2" fill="#fff"/><circle cx="22" cy="15" r="2" fill="#fff"/></svg>Campingblog</div>
    <div class="nav-item" style="left:944px">
      <svg viewBox="0 0 44 30" width="44"><rect x="2" y="4" width="38" height="20" rx="4" fill="#111"/><rect x="8" y="8" width="10" height="7" fill="#fff"/><rect x="22" y="8" width="12" height="7" fill="#fff"/><circle cx="24" cy="26" r="4" fill="#111" stroke="#fff" stroke-width="2"/></svg>Was ist Zeltwiese?</div>
    <div class="nav-item" style="left:1126px">
      <svg viewBox="0 0 24 30" width="24"><circle cx="12" cy="9" r="6" fill="#111"/><path d="M2 28c0-8 4-12 10-12s10 4 10 12z" fill="#111"/></svg>Anmelden</div>
  </nav>
</header>

<section class="search-band">
  <div class="search-field">
    <svg width="24" height="34" viewBox="0 0 24 34"><path d="M12 1C6 1 1 6 1 12c0 8 11 20 11 20s11-12 11-20C23 6 18 1 12 1z" fill="var(--green)"/><circle cx="12" cy="12" r="4" fill="#fff"/></svg>
    Nordsee
  </div>
  <div class="search-btn">Suchen</div>
</section>

<h1 class="page-title">Top Filter</h1>

<aside>
  <div class="map-teaser">
    <div class="map-art" role="img" aria-label="Stadtkartenausschnitt als Vorschau für die Kartensuche">
      <div class="map-label">Zur Karte</div>
    </div>
  </div>

  <div class="filter-box">
    <h3>Beliebteste Filter</h3>
    <ul class="filter-list">
      <li><span class="filter-icon"><svg width="24" height="18" viewBox="0 0 24 18" fill="none" stroke="#999" stroke-width="2"><path d="M2 6a15 15 0 0 1 20 0M5 10a10 10 0 0 1 14 0M8 14a5 5 0 0 1 8 0"/></svg></span>Gratis Wlan</li>
      <li><span class="filter-icon"><svg width="22" height="20" viewBox="0 0 22 20" fill="#999"><circle cx="5" cy="6" r="2.5"/><circle cx="9" cy="3" r="2.5"/><circle cx="14" cy="3" r="2.5"/><circle cx="18" cy="6" r="2.5"/><ellipse cx="11.5" cy="14" rx="6" ry="5"/></svg></span>Hunde willkommen</li>
      <li><span class="filter-icon"><svg width="24" height="22" viewBox="0 0 24 22" fill="none" stroke="#999" stroke-width="1.6"><path d="M7 14V3h6v11M7 7h6M2 16c3-2 4 2 7 0s4 2 7 0 4 2 6 0M2 20c3-2 4 2 7 0s4 2 7 0 4 2 6 0"/></svg></span>Pool/Freibad</li>
      <li><span class="filter-icon"><svg width="26" height="24" viewBox="0 0 26 24" fill="#999"><circle cx="7" cy="3" r="2.5"/><rect x="4" y="6" width="6" height="9"/><rect x="4.5" y="15" width="2" height="8"/><rect x="7.5" y="15" width="2" height="8"/><circle cx="19" cy="3" r="2.5"/><path d="M15 7h8l1 9h-10z"/><rect x="16.5" y="15" width="2" height="8"/><rect x="19.5" y="15" width="2" height="8"/></svg></span>FKK-Bereich</li>
      <li><span class="filter-icon"><svg width="26" height="24" viewBox="0 0 26 24" fill="none" stroke="#999" stroke-width="1.6"><path d="M2 10a11 8 0 0 1 22 0zM13 10v12M4 22h18"/></svg></span>Nähe Strand</li>
      <li><span class="filter-icon"><svg width="22" height="24" viewBox="0 0 22 24" fill="none" stroke="#999" stroke-width="1.8"><circle cx="8" cy="3" r="2" fill="#999"/><path d="M8 6v8h7l3 6M8 10h6"/><path d="M6 12a6 6 0 1 0 8 8"/></svg></span>Rollstuhlgerecht</li>
    </ul>
    <div class="more-filters">Weitere Filter <svg width="14" height="12" viewBox="0 0 14 12"><path d="M0 0h14L7 12z" fill="#111"/></svg></div>
  </div>

  <div class="ad-note" style="left:32px;top:898px">Anzeige</div>
  <div class="rect-ad"><strong>Größe eines<br>Rectangle Banners</strong><span>(300 × 250 Pixel)</span></div>
</aside>

<main>
  <article class="camp-card" style="top:265px">
    <div class="camp-photo" role="img" aria-label="Foto: Einfahrt zum Campingplatz zwischen hohen Bäumen" style="background:linear-gradient(180deg,#cfd6d6 0%,#5f6e4e 45%,#7b7a72 75%,#6a6a66 100%)"></div>
    <div class="camp-body">
      <h2>Campingplatz Am Heidehang</h2>
      <p class="camp-desc">Der Campingplatz Am Heidehang ist ein von vielen Baumreihen durchzogenes Heidegelände. Die Stellplätze sind durch naturhecken abgeteilt, der Zeltplatz liegt separat.</p>
      <div class="camp-meta"><span>Ort: 29600 Heidedorf</span><span>Bundesland: Niedersachsen</span><span>Land: Deutschland</span><span>Region: Lüneburger Heide</span><span>Vergleichspreis: k. A.</span></div>
      <a class="camp-link">Zur Detailseite</a>
    </div>
  </article>

  <div class="banner-ad" style="top:524px">
    <div class="banner-art" role="img" aria-label="Illustration eines blauen Ferienhauses" style="left:14px;width:120px;background:linear-gradient(180deg,#0a6fc9,#2b8ee0 60%,#1a78cf)"></div>
    <div class="banner-text"><strong>Mit Urlaub Geld verdienen</strong><span>Urlaub steht vor der Tür? So viel können Sie<br>verdienen, während Sie unterwegs sind.</span></div>
    <div class="banner-art" role="img" aria-label="Illustration eines Ferienhauses mit Garten" style="left:510px;width:110px;background:linear-gradient(180deg,#dfe6ec,#c9c2a8 60%,#6aa53a)"></div>
    <div class="banner-brand">Logis Sofort</div>
    <div class="banner-btn">Mehr erfahren</div>
  </div>
  <div class="ad-label" style="top:629px">Werbung</div>

  <article class="camp-card" style="top:665px">
    <div class="camp-photo" role="img" aria-label="Luftbild: Campingplatz am Flussufer mit Wiesen und Bäumen" style="background:linear-gradient(180deg,#8a9a78 0%,#5d7a45 40%,#4d6b86 60%,#34506a 100%)"></div>
    <div class="camp-body">
      <h2>Campingplatz Elbwiese</h2>
      <p class="camp-desc">Der Campingplatz Elbwiese ist ein ebener Campingplatz direkt an der Elbe mit gepflegtem Wiesengelände und einem kleinen Teich. Der weitläufige Platz bietet teilweise sogar Stellplätze direkt an der Elbe. Die Nähe zur Weltstadt Hamburg bietet viele Ausflugsmöglichkeiten.</p>
      <div class="camp-meta" style="top:155px"><span>Ort: 21400 Elbhusen</span><span>Bundesland: Niedersachsen</span><span>Land: Deutschland&nbsp; Region:</span><span>Lüneburger Heide</span><span>Vergleichspreis: 25,00 €</span></div>
      <a class="camp-link">Zur Detailseite</a>
    </div>
  </article>

  <article class="camp-card" style="top:923px">
    <div class="camp-photo" role="img" aria-label="Foto: Einfahrt zum Campingplatz zwischen hohen Bäumen" style="background:linear-gradient(180deg,#cfd6d6 0%,#5f6e4e 45%,#7b7a72 75%,#6a6a66 100%)"></div>
    <div class="camp-body">
      <h2>Campingplatz Am Heidehang</h2>
      <p class="camp-desc">Der Campingplatz Am Heidehang ist ein von vielen Baumreihen durchzogenes Heidegelände. Die Stellplätze sind durch naturhecken abgeteilt, der Zeltplatz liegt separat.</p>
      <div class="camp-meta"><span>Ort: 29600 Heidedorf</span><span>Bundesland: Niedersachsen</span><span>Land: Deutschland</span><span>Region: Lüneburger Heide</span><span>Vergleichspreis: k. A.</span></div>
      <a class="camp-link">Zur Detailseite</a>
    </div>
  </article>

  <article class="camp-card" style="top:1179px">
    <div class="camp-photo" role="img" aria-label="Luftbild: Campingplatz im grünen Tal mit Wald" style="background:linear-gradient(180deg,#6d8a52 0%,#4f7a36 45%,#8f9f80 70%,#3f6a2a 100%)"></div>
    <div class="camp-body">
      <h2>Camping Maintal Park</h2>
      <p class="camp-desc">Der Campingplatz Am Heidehang ist ein von vielen Baumreihen durchzogenes Heidegelände. Die Stellplätze sind durch naturhecken abgeteilt, der Zeltplatz liegt separat.</p>
      <div class="camp-meta"><span>Ort: 29600 Heidedorf</span><span>Bundesland: Niedersachsen</span><span>Land: Deutschland</span><span>Region: Lüneburger Heide</span><span>Vergleichspreis: k. A.</span></div>
      <a class="camp-link">Zur Detailseite</a>
    </div>
  </article>

  <div class="banner-ad" style="top:1437px">
    <div class="banner-art" role="img" aria-label="Illustration eines blauen Ferienhauses" style="left:14px;width:120px;background:linear-gradient(180deg,#0a6fc9,#2b8ee0 60%,#1a78cf)"></div>
    <div class="banner-text"><strong>Mit Urlaub Geld verdienen</strong><span>Urlaub steht vor der Tür? So viel können Sie<br>verdienen, während Sie unterwegs sind.</span></div>
    <div class="banner-art" role="img" aria-label="Illustration eines Ferienhauses mit Garten" style="left:510px;width:110px;background:linear-gradient(180deg,#dfe6ec,#c9c2a8 60%,#6aa53a)"></div>
    <div class="banner-brand">Logis Sofort</div>
    <div class="banner-btn">Mehr erfahren</div>
  </div>
  <div class="ad-label" style="top:1542px">Werbung</div>
</main>

<footer class="site-footer">
  <div class="footer-col"><h2 style="left:35px">Warum Zeltwiese?</h2>
    <p class="footer-text">Lorem ipsum dolor sit amet, consetetur sadipscing elitr, sed diam nonumy eirmod tempor invidunt ut labore et dolore magna aliquyam erat, sed diam voluptua. At vero eos et accusam et justo duo dolores et ea rebum. Stet clita kasd gubergren, no sea takimata sanctus est Lorem ipsum dolor sit amet. Lorem ipsum dolor sit amet, consetetur sadipscing elitr, sed diam nonumy eirmod tempor invidunt ut labore et dolore magna aliquyam erat, sed diam voluptua. At vero eos et accusam et justo duo dolores et ea rebum. Stet clita kasd gubergren, no sea takimata sanctus est</p>
  </div>
  <div class="footer-col"><h2 style="left:522px;top:22px">Top Regionen</h2>
    <ul class="link-col" style="left:522px"><li>Allgäu</li><li>Südtirol</li><li>Mallorca</li><li>Tirol</li><li>Oberstdorf</li><li>Fuerteventura</li><li>Sardinien</li><li>Schwarzwald</li><li>Schweiz</li></ul>
    <ul class="link-col" style="left:698px"><li>Bayerischen</li><li>Wald</li><li>Teneriffa</li><li>Harz</li><li>Gran Canaria</li><li>Bayerischen</li><li>Wald</li><li>Teneriffa</li><li>Harz</li></ul>
  </div>
  <div class="footer-col"><h2 style="left:897px;top:22px">Top Städte</h2>
    <ul class="link-col" style="left:902px"><li>Berlin</li><li>Rostock</li><li>Frankfurt</li><li>Köln</li><li>Paris</li><li>St. Tropez</li><li>München</li><li>Toulouse</li><li>Rom</li></ul>
    <ul class="link-col" style="left:1048px"><li>Berlin</li><li>Rostock</li><li>Frankfurt</li><li>Köln</li><li>Paris</li><li>St. Tropez</li><li>München</li><li>Toulouse</li><li>Rom</li></ul>
  </div>
  <div class="footer-rule"></div>
  <div class="footer-social">
    <div class="brand" style="position:static"><span class="brand-dot"></span>zeltwiese</div>
    <span class="social"><span class="social-dot"></span>Freundbuch</span>
    <span class="social"><span class="social-dot"></span>Zwitscher</span>
    <span class="social"><span class="social-dot"></span>Suchlux+</span>
    <span class="social"><span class="social-dot"></span>Klipptube</span>
    <span class="mail-btn"><svg width="26" height="18" viewBox="0 0 26 18" fill="none" stroke="#fff" stroke-width="2"><rect x="1" y="1" width="24" height="16" rx="2"/><path d="M1 2l12 9 12-9"/></svg></span>
  </div>
  <div class="footer-links">Campingplatz anmelden&nbsp; | &nbsp;Sitemap&nbsp; | &nbsp;Kontakt&nbsp; | &nbsp;Impressum&nbsp; | &nbsp; © 2013-2015 Zeltwiese</div>
</footer>

</div>
</body>
</html>
```